Etiketten für Kosmetik Produkte  100% Natural Made in Germany
Etiketten für Kosmetik Produkte 100% Natural Made in Germany
Zielgruppe
auf Hochwertige -zertifizierte Naturprodukte wert legen.
Hergestellt in Deutschland und Verpackt
Aufgabenstellung
Hallo ihr lieben,
für die SilbTau Kosmetik - wünschen wir einen neuen frischen Style - das dunkle Etikett möchten wir los werden.
Ein helles frisches Design
Zielgruppe- alle die auf Hochwertige - zertifizierte Naturprodukte bevorzugen
Die Produkte haben mit eine VERUN Zertifizierung - Höchste Qalität an Naturprodukte
Das Glas was wir nutzen ist ein violettes Glas und sehr hochwertig was wir beibehalten möchten.
Das Produkt ist dadurch sehr Geschütz und nachhaltig dazu
Es sind 12 Produkte - Design bleibt bei allen gleich.
Design Wunsch -!!!!
Was gut zum Glas Passt- nur kein schwarz bitte
und Produkt gut passt
Weiß - Kupfer eventuell
Kein Muss - sind für alles offen ( nur kein schwarz
Logo - Name bleibt :-)
Das Design von Tesoro Naturkosmetik
Gefällt uns sehr gut in der Richtung
Was die Natürlichkeit- Reinheit - Qualität
Verkörpert:-)
Fotos zum Prosukt:
Hier ein link zum Instagram
https://instagram.com/lumaroze.spain?igshid=MzRlODBiNWFlZA==
https://instagram.com/silbtau_naturkosmetik?igshid=MzRlODBiNWFlZA==
An den Flyer den wir hochgeladen kann man sehen um welche Produkte es sich handelt und auch im Instagram zu sehen sind.
Wenn ihr weitere Fotos benötigen tut- bitte melden
Viel Glück :-) danke für eure Unterstützung

```html
<!DOCTYPE html>
<html lang="de">
<head>
<meta charset="utf-8">
<title>SilbTau Naturkosmetik – Etikett Lemon &amp; Orange Oil</title>
<link rel="stylesheet" href="https://fonts.googleapis.com/css2?family=Marcellus&family=Montserrat:wght@400;700&display=swap">
<style>
  :root {
    --page-bg: #ffffff;
    --rim: #f4ede6;
    --rim-edge: #d8b79c;
    --label-center: #fdfaf6;
    --copper-light: #f2cfb0;
    --copper-mid: #dca07a;
    --copper-deep: #b8744c;
    --brand-copper: #a8613a;
    --ink-warm: #5a3220;
    --divider: #c98a5c;
  }
  html, body {
    margin: 0;
    padding: 0;
    width: 1200px;
    height: 960px;
    overflow: hidden;
    background: var(--page-bg);
  }
  .label-canvas {
    display: block;
    width: 1200px;
    height: 960px;
  }
  .ring-text {
    font-family: "Montserrat", sans-serif;
    font-weight: 400;
    font-size: 40px;
    letter-spacing: 20px;
    fill: var(--ink-warm);
  }
  .brand-name {
    font-family: "Marcellus", serif;
    font-size: 80px;
    letter-spacing: 2px;
    fill: var(--brand-copper);
  }
  .brand-sub {
    font-family: "Marcellus", serif;
    font-size: 34px;
    letter-spacing: 1px;
    fill: var(--brand-copper);
  }
  .category-bold {
    font-family: "Montserrat", sans-serif;
    font-weight: 700;
    font-size: 24px;
    fill: var(--ink-warm);
  }
  .category-light {
    font-family: "Montserrat", sans-serif;
    font-weight: 400;
    font-size: 24px;
    fill: var(--ink-warm);
  }
</style>
</head>
<body>
<svg class="label-canvas" viewBox="0 0 1200 960" xmlns="http://www.w3.org/2000/svg">
  <defs>
    <linearGradient id="copper-band" x1="0" y1="0" x2="1" y2="1">
      <stop offset="0" stop-color="var(--copper-deep)"/>
      <stop offset="0.35" stop-color="var(--copper-light)"/>
      <stop offset="0.7" stop-color="var(--copper-mid)"/>
      <stop offset="1" stop-color="var(--copper-deep)"/>
    </linearGradient>
    <path id="ring-top" d="M 285 480 A 315 315 0 0 1 915 480"/>
    <path id="ring-bottom" d="M 255 480 A 345 345 0 0 0 945 480"/>
  </defs>

  <g class="lid-label">
    <circle class="lid-rim" cx="600" cy="480" r="428" fill="var(--rim)" stroke="var(--rim-edge)" stroke-width="4"/>
    <circle class="copper-band" cx="600" cy="480" r="372" fill="url(#copper-band)"/>
    <circle class="label-center" cx="600" cy="480" r="290" fill="var(--label-center)"/>

    <text class="ring-text"><textPath href="#ring-top" startOffset="50%" text-anchor="middle">LEMON &amp; ORANGE OIL</textPath></text>
    <text class="ring-text"><textPath href="#ring-bottom" startOffset="50%" text-anchor="middle">LEMON &amp; ORANGE OIL</textPath></text>
    <circle class="ring-dot" cx="270" cy="480" r="8" fill="var(--ink-warm)"/>
    <circle class="ring-dot" cx="930" cy="480" r="8" fill="var(--ink-warm)"/>

    <circle class="brand-mark" cx="600" cy="320" r="58" fill="none" stroke="var(--brand-copper)" stroke-width="4"/>
    <text class="brand-name" x="600" y="470" text-anchor="middle">SILBTAU</text>
    <text class="brand-sub" x="600" y="520" text-anchor="middle">NATURKOSMETIK</text>

    <text class="category-bold" x="588" y="640" text-anchor="end">BODY CARE</text>
    <line class="category-divider" x1="608" y1="610" x2="596" y2="660" stroke="var(--divider)" stroke-width="2"/>
    <text class="category-light" x="616" y="640" text-anchor="start">ORGANIC</text>
  </g>
</svg>
</body>
</html>
```